Funky Modern Flyer A5 or Postcard size

Hi, I am looking at a one small flyer (A5 or postcard size) that I can put both on my website on the front page (ie so png) and also send out if necessary.

It has to be modern, funky and hip. My brand is professional / Corporate so it also has to fit in with that brand.

There are 6 attachments:
Example 1 - Kavorra - I like this look, clean, modern, funky and says it all.
Example 2 - Kavora - again another look I like, simple, explanatory
Example 4 - Artisan Bazaar - font is cool on this one but background not so much too much going on but I like the font
Example 5 - Example 4 - Artisan Bazaar - font is cool on this one but background not so much too much going on but I like the font
5 is my logo
Example 6 is something I found on the web this morning which is effective.

It is for a Mentoring and Training program I run called: SKYWARD

What is to be included is the following:
The name: Skyward
Somewhere: Training, Mentoring
My Logo (see attached two options) you can choose which colour suits and I have the source file should you need it
My website and email: www.deliamarsk.example / delia@deliamarsk.example

This wording: This is one of our highest in-demand programs and is based on a background and proven track record by Delia in accelerating sales organisations and their people into stand out high performers. **(NOTE this wording in this paragraph may change and I am open to you changing if you think you can make it more effective!)

Colours: white, black and gold (those are our website colours).

I'd like the Skyward to really stand out.... I have included two fonts that I really like that I got off Artisan Bazaar. However, feel free to suggest other fonts that you think cool or funky!
Updates

Hi everyone, just to add a note to the brief, I am not overly keen on pictures that are really busy. I only like a picture that is minimal and effective. The examples from Artisan Bazaar was more for the Font Style not so much the pictures in the background. The pictures can take away from a design unless done really minimally.....hope this makes sense. Delia Added Wednesday, March 15, 2017

Target Market(s)

My target Market is Corporates but I want a Funky Modern look as a lot of people in Corporates are Millennials as well which is part of my target market

Industry/Entity Type

Information Technology

Requirements
Must have
• What is to be included is the following:
• The name: Skyward
• Somewhere: Training, Mentoring
• My Logo (see attached two options) you can choose which colour suits and I have the source file should you need it
• My website and email: www.deliamarsk.example / delia@deliamarsk.example
• This wording: This is one of our highest in-demand programs and is based on a background and proven track record in high performance and accelerating sales organisations and their people into stand out high performers. (**NOTE this wording may change when final design is picked to be changed as still working in it***)
• Colours: white, black and gold (those are our website colours).
• I'd like the Skyward to really stand out.... I have included two fonts that I really like that I got off Artisan Bazaar. However, feel free to suggest other fonts that you think cool or funky! NOTE: The pictures I have attached is mainly for the FONTS not for the background pictures. I am not that keen on background pictures as it can take away from the font - unless it is minimal
Should not have
• Too many different colours, I like slick, modern, clean. White, gold and black preferred as this is our website colour.
• NOTE: The pictures from Artisan Bazaar I have attached are mainly for the FONTS not for the background pictures. I am not hugely keen on background pictures as it can take away from the font/message - unless the pictures are minimal but effective.

```html
<!DOCTYPE html>
<html lang="en">
<head>
<meta charset="utf-8">
<title>Skyward – Flyer Variants</title>
<link rel="stylesheet" href="https://fonts.googleapis.com/css2?family=Kaushan+Script&family=Lato:wght@400;700&family=Oswald:wght@600&family=Roboto:wght@300&family=Roboto+Condensed:wght@400&display=swap">
<style>
  :root{
    --gold:#c9a03a;
    --gold-light:#e9c55c;
    --gold-deep:#a9802a;
    --cream:#f6e9a9;
    --ink:#1b1b1b;
    --paper:#f3f3f3;
    --charcoal:#3b3b3c;
    --stage:#e7e4df;
    --photo-dark:#1e2a63;
    --photo-mid:#4b4f94;
    --photo-light:#8a86bd;
    --glow:#6fb8ff;
  }
  *{margin:0;padding:0;box-sizing:border-box}
  html,body{width:1200px;height:1200px;overflow:hidden}
  body{background:var(--stage);position:relative}

  .flyer{
    position:absolute;top:215px;width:543px;height:769px;overflow:hidden;
    box-shadow:0 6px 18px rgba(0,0,0,.25);
  }
  .flyer--light{left:37px;--bg:var(--paper);--name:#6a6a6a;--text:var(--ink);
    background:linear-gradient(160deg,#ffffff 0%,var(--paper) 55%,#e9e9e9 100%)}
  .flyer--dark{left:621px;--bg:var(--charcoal);--name:var(--gold);--text:#ffffff;
    background:linear-gradient(160deg,#454546 0%,var(--charcoal) 55%,#333334 100%)}

  .brand-name{
    position:absolute;top:66px;left:0;width:100%;text-align:center;
    font-family:"Roboto",sans-serif;font-weight:300;font-size:19px;letter-spacing:1.5px;
    color:var(--name);
  }

  .band-top-accent{position:absolute;left:0;top:94px;width:139px;height:8px;
    background:linear-gradient(90deg,var(--gold-deep),var(--gold-light));
    clip-path:polygon(0 0,100% 0,88% 100%,0 100%)}
  .rule{position:absolute;left:0;width:100%;height:4px;background:#ffffff}
  .rule--top{top:100px}
  .rule--bottom{top:362px}

  .hero-photo{
    position:absolute;left:0;top:104px;width:100%;height:258px;
    background:
      radial-gradient(circle at 48% 57%,rgba(180,225,255,.95) 0,var(--glow) 4%,rgba(70,120,230,.55) 13%,transparent 26%),
      linear-gradient(90deg,var(--photo-dark) 0%,#2d3a80 35%,var(--photo-mid) 60%,var(--photo-light) 100%);
  }
  .band-photo-accent{position:absolute;right:0;top:366px;width:120px;height:9px;
    background:linear-gradient(90deg,var(--gold-light),var(--gold));
    clip-path:polygon(12% 0,100% 0,100% 100%,0 100%)}

  .headline{
    position:absolute;top:398px;left:0;width:100%;text-align:center;
    font-family:"Oswald",sans-serif;font-weight:600;font-size:46px;line-height:54px;letter-spacing:1px;
    background:linear-gradient(180deg,var(--gold-light) 0%,var(--gold) 55%,var(--gold-deep) 100%);
    -webkit-background-clip:text;background-clip:text;color:transparent;
  }
  .program-name{
    position:absolute;top:498px;left:0;width:100%;text-align:center;
    font-family:"Kaushan Script",cursive;font-size:78px;line-height:100px;color:var(--gold);
  }
  .services{
    position:absolute;top:614px;left:0;width:100%;text-align:center;
    font-family:"Lato",sans-serif;font-size:24px;color:var(--text);
  }
  .blurb{
    position:absolute;top:656px;left:28px;right:28px;text-align:center;
    font-family:"Lato",sans-serif;font-size:14px;line-height:17px;color:var(--text);
  }

  .footer{position:absolute;left:0;bottom:0;width:100%;height:35px;
    background:linear-gradient(90deg,var(--gold-deep),var(--gold-light) 50%,var(--gold-deep));
    border-bottom:3px solid var(--ink)}
  .footer__panel{position:absolute;left:92px;top:0;width:376px;height:32px;
    background:var(--cream);clip-path:polygon(6% 0,100% 0,94% 100%,0 100%)}
  .footer__contacts{position:absolute;left:0;top:0;width:100%;height:32px;
    display:flex;justify-content:center;align-items:center;gap:9px;
    font-family:"Roboto Condensed",sans-serif;font-size:11.5px;color:var(--ink)}
  .contact{display:flex;align-items:center;gap:4px}
  .contact svg{width:10px;height:10px}
</style>
</head>
<body>

  <section class="flyer flyer--light">
    <div class="brand-name">DELIA MARSK</div>
    <div class="band-top-accent"></div>
    <div class="rule rule--top"></div>
    <div class="hero-photo" role="img" aria-label="Photo of a hand touching a glowing blue digital marketing interface"></div>
    <div class="rule rule--bottom"></div>
    <div class="band-photo-accent"></div>
    <h1 class="headline">EXCLUTIVE DIGITAL<br>SALES STRATEGIST</h1>
    <div class="program-name">Skyward</div>
    <p class="services">Training, Mentoring</p>
    <p class="blurb">This is one of our highest in-demand programs and is based on a background and proven track record by Delia in accelerating sales organisations and their people into stand out high performers.</p>
    <footer class="footer">
      <div class="footer__panel"></div>
      <div class="footer__contacts">
        <span class="contact"><svg viewBox="0 0 10 10"><circle cx="5" cy="5" r="4.5" fill="#1b1b1b"/><path d="M.5 5h9M5 .5c-2 2.5-2 6.5 0 9M5 .5c2 2.5 2 6.5 0 9" stroke="#f6e9a9" stroke-width=".7" fill="none"/></svg>www.deliamarsk.example</span>
        <span class="contact"><svg viewBox="0 0 10 10"><rect x=".5" y="2" width="9" height="6.5" fill="#1b1b1b"/><path d="M.5 2l4.5 3.5L9.5 2" stroke="#f6e9a9" stroke-width=".8" fill="none"/></svg>delia@deliamarsk.example</span>
      </div>
    </footer>
  </section>

  <section class="flyer flyer--dark">
    <div class="brand-name">DELIA MARSK</div>
    <div class="band-top-accent"></div>
    <div class="rule rule--top"></div>
    <div class="hero-photo" role="img" aria-label="Photo of a hand touching a glowing blue digital marketing interface"></div>
    <div class="rule rule--bottom"></div>
    <div class="band-photo-accent"></div>
    <h1 class="headline">EXCLUTIVE DIGITAL<br>SALES STRATEGIST</h1>
    <div class="program-name">Skyward</div>
    <p class="services">Training, Mentoring</p>
    <p class="blurb">This is one of our highest in-demand programs and is based on a background and proven track record by Delia in accelerating sales organisations and their people into stand out high performers.</p>
    <footer class="footer">
      <div class="footer__panel"></div>
      <div class="footer__contacts">
        <span class="contact"><svg viewBox="0 0 10 10"><circle cx="5" cy="5" r="4.5" fill="#1b1b1b"/><path d="M.5 5h9M5 .5c-2 2.5-2 6.5 0 9M5 .5c2 2.5 2 6.5 0 9" stroke="#f6e9a9" stroke-width=".7" fill="none"/></svg>www.deliamarsk.example</span>
        <span class="contact"><svg viewBox="0 0 10 10"><rect x=".5" y="2" width="9" height="6.5" fill="#1b1b1b"/><path d="M.5 2l4.5 3.5L9.5 2" stroke="#f6e9a9" stroke-width=".8" fill="none"/></svg>delia@deliamarsk.example</span>
      </div>
    </footer>
  </section>

</body>
</html>
```